Appliance Retail store requires an 8 page Advertising Flyer designed

Size of the catalogue: 275 mm x 180 mm
We will be needing 8 pages.

We need a bright, exciting catalogue designed. This catalogue will be used for letterbox delivery to customers and also for public handouts.

We are an Outlet Store as well as Importer and focus on providing the best possible deals around. Our corporate colors are bright green. I have included a mock up of our new store, and old price ticket, logo etc.

There is a zip file with 6 of the 8 pages including text, this should give a very good start for anyone. this site shows you a layout we like a lot, and would like to follow something similar. >>> http://www.quarvexsonic.co.nz <<< NOTE! we want our booklet to look like this with our colours !!! check the attached files, do not send anything wildly different from this !!

For the initial entries, I'm expecting to see the cover page and one inner page.

Industry/Entity Type

Retail

Colors
9ccb3c

Requirements
Must have
• i want pretty much the same look as flyer and flyer1 (files 9 and 10) just with our very bright green and the rest of the colors i will leave up to you

```html
<!DOCTYPE html>
<html lang="en">
<head>
<meta charset="utf-8">
<title>Volterra Outlet – Catalogue</title>
<link href="https://fonts.googleapis.com/css2?family=Open+Sans:wght@400;600;700;800&display=swap" rel="stylesheet">
<style>
:root{
  --green:#9ccb3c;
  --green-dark:#6fa821;
  --ink:#3a3a3a;
  --muted:#8a8a8a;
  --paper:#ffffff;
  --backdrop:#d6d6d6;
  --photo-a:#5d6a66;
  --photo-b:#b9c3c4;
  --product-a:#e4e6e8;
  --product-b:#aeb3b8;
}
*{box-sizing:border-box;margin:0;padding:0}
html,body{width:773px;height:1200px;overflow:hidden}
body{background:var(--backdrop);font-family:"Open Sans",Arial,sans-serif;color:var(--ink);position:relative}

/* cover */
.cover{position:absolute;left:76px;top:50px;width:620px;height:405px;background:var(--paper);box-shadow:0 2px 8px rgba(0,0,0,.18)}
.cover-rule{position:absolute;left:0;right:0;top:24px;height:4px;background:var(--green)}
.cover-photo{position:absolute;left:0;right:0;top:30px;height:200px;background:linear-gradient(180deg,var(--photo-b) 0%,var(--photo-a) 100%)}
.cover-band{position:absolute;left:0;right:0;top:232px;height:10px;background:linear-gradient(90deg,var(--green-dark),var(--green) 60%,#d6ecae)}
.cover-band.thin{top:246px;height:3px;opacity:.7}
.cover-url{position:absolute;right:26px;top:270px;font-size:10px;font-weight:600;color:var(--muted)}
.cover-url-rule{position:absolute;right:26px;top:287px;width:200px;height:1px;background:var(--green)}
.brand{position:absolute;left:50%;top:318px;transform:translateX(-50%);display:flex;align-items:center;gap:8px}
.brand-mark{width:18px;height:18px;background:var(--green)}
.brand-name{font-size:15px;font-weight:700;color:var(--green-dark);letter-spacing:1px;text-transform:uppercase}

/* spreads */
.spread{position:absolute;left:26px;width:720px;height:236px;display:flex;box-shadow:0 2px 8px rgba(0,0,0,.18)}
.spread.about{top:525px}
.spread.range{top:835px}
.page{position:relative;width:360px;height:100%;background:var(--paper);padding:22px 22px}
.page.left{background:linear-gradient(90deg,#fff 88%,#ececec)}
.page.right{background:linear-gradient(90deg,#ececec,#fff 12%)}
.section-no{font-size:20px;font-weight:800;color:var(--ink)}
.section-rule{height:2px;background:var(--green);margin:4px 0 14px;width:100%}
.section-title{font-size:13px;font-weight:700;color:var(--green-dark);margin-bottom:6px}
.body-copy{font-size:7px;line-height:1.55;color:var(--muted);width:150px}

.about .page.right{display:flex;gap:14px;padding-top:40px}
.about .body-copy{width:110px}
.product-grid{display:grid;grid-template-columns:repeat(3,56px);grid-template-rows:repeat(2,64px);gap:8px}
.product-shot{background:linear-gradient(160deg,var(--product-a),var(--product-b));border:1px solid #ddd}

.card-grid{display:grid;grid-template-columns:1fr 1fr;gap:10px 14px}
.range .page.right .card-grid{margin-top:36px}
.card{display:flex;gap:6px;align-items:flex-start}
.card-shot{flex:0 0 22px;height:32px;background:linear-gradient(160deg,var(--product-a),var(--product-b));border:1px solid #ddd}
.card-title{font-size:6.5px;font-weight:700;color:var(--green-dark);margin-bottom:2px}
.card-text{font-size:6px;line-height:1.4;color:var(--muted)}
</style>
</head>
<body>

<section class="cover">
  <div class="cover-rule"></div>
  <div class="cover-photo" role="img" aria-label="Photograph of the Volterra Outlet store front with green signage and cars in the car park"></div>
  <div class="cover-band"></div>
  <div class="cover-band thin"></div>
  <p class="cover-url">www.volterraoutlet.co.nz</p>
  <div class="cover-url-rule"></div>
  <div class="brand"><span class="brand-mark"></span><span class="brand-name">Volterra Outlet</span></div>
</section>

<section class="spread about">
  <div class="page left">
    <p class="section-no">01</p>
    <div class="section-rule"></div>
    <h2 class="section-title">About us</h2>
    <p class="body-copy">We are an independent outlet store and importer bringing you quality home appliances at the best possible prices. Visit our showroom to see the full range in person.</p>
  </div>
  <div class="page right">
    <p class="body-copy">Every product is checked by our team before it reaches the floor, so you shop with full confidence.</p>
    <div class="product-grid">
      <div class="product-shot" role="img" aria-label="Front loading washing machine"></div>
      <div class="product-shot" role="img" aria-label="Steam oven"></div>
      <div class="product-shot" role="img" aria-label="Red microwave"></div>
      <div class="product-shot" role="img" aria-label="Freestanding oven"></div>
      <div class="product-shot" role="img" aria-label="Fridge freezer"></div>
      <div class="product-shot" role="img" aria-label="Stainless range hood"></div>
    </div>
  </div>
</section>

<section class="spread range">
  <div class="page left">
    <p class="section-no">02</p>
    <div class="section-rule"></div>
    <div class="card-grid">
      <div class="card"><div class="card-shot" role="img" aria-label="Washer"></div><div><p class="card-title">Front Washer</p><p class="card-text">Energy rated, quiet running, two year warranty.</p></div></div>
      <div class="card"><div class="card-shot" role="img" aria-label="Steam oven"></div><div><p class="card-title">Steam Oven</p><p class="card-text">Energy rated, quiet running, two year warranty.</p></div></div>
      <div class="card"><div class="card-shot" role="img" aria-label="Freezer"></div><div><p class="card-title">Upright Freezer</p><p class="card-text">Energy rated, quiet running, two year warranty.</p></div></div>
      <div class="card"><div class="card-shot" role="img" aria-label="Wall oven"></div><div><p class="card-title">Wall Oven</p><p class="card-text">Energy rated, quiet running, two year warranty.</p></div></div>
      <div class="card"><div class="card-shot" role="img" aria-label="Fridge freezer"></div><div><p class="card-title">Fridge Freezer</p><p class="card-text">Energy rated, quiet running, two year warranty.</p></div></div>
      <div class="card"><div class="card-shot" role="img" aria-label="Dish drawer"></div><div><p class="card-title">Dish Drawer</p><p class="card-text">Energy rated, quiet running, two year warranty.</p></div></div>
    </div>
  </div>
  <div class="page right">
    <div class="card-grid">
      <div class="card"><div class="card-shot" role="img" aria-label="Heat pump"></div><div><p class="card-title">Heat Pump</p><p class="card-text">Energy rated, quiet running, two year warranty.</p></div></div>
      <div class="card"><div class="card-shot" role="img" aria-label="Microwave"></div><div><p class="card-title">Microwave Combo</p><p class="card-text">Energy rated, quiet running, two year warranty.</p></div></div>
      <div class="card"><div class="card-shot" role="img" aria-label="Chest freezer"></div><div><p class="card-title">Chest Freezer</p><p class="card-text">Energy rated, quiet running, two year warranty.</p></div></div>
      <div class="card"><div class="card-shot" role="img" aria-label="Gas cooktop"></div><div><p class="card-title">Gas Cooktop</p><p class="card-text">Energy rated, quiet running, two year warranty.</p></div></div>
      <div class="card"><div class="card-shot" role="img" aria-label="Range hood"></div><div><p class="card-title">Range Hood</p><p class="card-text">Energy rated, quiet running, two year warranty.</p></div></div>
      <div class="card"><div class="card-shot" role="img" aria-label="Clothes dryer"></div><div><p class="card-title">Clothes Dryer</p><p class="card-text">Energy rated, quiet running, two year warranty.</p></div></div>
    </div>
  </div>
</section>

</body>
</html>
```